business card for a massage therapy practice named 'Meadow and Rowan Massage Studio'

I really need a trendy, yet easy on the eyes business card to complement my logo. Ideally with some gold or rose gold foil work.

My uploaded file of the logo I have in horizontal but I have a vertical version as well. Another color that is used in the website is a blush pink here and there. I'd like to see some trendy tropical leaves in the design.

```html
<!DOCTYPE html>
<html lang="en">
<head>
<meta charset="utf-8">
<title>Meadow and Rowan Massage Studio – Business Card</title>
<link href="https://fonts.googleapis.com/css2?family=Open+Sans:wght@400;600&family=Allura&display=swap" rel="stylesheet">
<style>
  :root {
    --backdrop: #2a2a2c;
    --card-dark: #141414;
    --card-light: #fbfbfa;
    --ink: #1c1c1c;
    --ink-soft: #6a6a6a;
    --mint: #7fd3bb;
    --gold-light: #e6d39c;
    --gold: #c2ad74;
    --gold-deep: #8f7a45;
    --silver: #c4c4c4;
  }
  * { margin: 0; padding: 0; box-sizing: border-box; }
  html, body {
    width: 1200px; height: 942px; overflow: hidden;
    background: var(--backdrop);
    font-family: "Open Sans", Arial, sans-serif;
  }
  .stage {
    width: 1200px; height: 942px;
    display: flex; align-items: center; justify-content: center; gap: 44px;
  }
  .card {
    width: 530px; height: 303px; border-radius: 22px; position: relative;
    box-shadow: 0 14px 30px rgba(0,0,0,.45);
    flex: none;
  }
  .mark-dot {
    width: 30px; height: 30px; border-radius: 50%; flex: none;
    background: radial-gradient(circle at 35% 30%, var(--gold-light), var(--gold) 55%, var(--gold-deep));
  }
  .brand-name {
    font-weight: 600; line-height: 1.25; letter-spacing: .4px;
    white-space: nowrap;
  }

  /* Front */
  .card-front { background: var(--card-dark); }
  .front-mark {
    position: absolute; left: 50%; top: 50%; transform: translate(-50%, -50%);
    display: flex; align-items: center; gap: 16px;
  }
  .card-front .brand-name { font-size: 23px; color: var(--silver); }

  /* Back */
  .card-back { background: var(--card-light); }
  .back-mark {
    position: absolute; right: 40px; top: 38px;
    display: flex; align-items: center; gap: 12px;
  }
  .back-mark .mark-dot { width: 24px; height: 24px; }
  .card-back .brand-name { font-size: 17px; color: var(--ink); }

  .person { position: absolute; left: 150px; top: 116px; }
  .person-name { font-family: "Allura", cursive; font-size: 42px; color: var(--ink-soft); line-height: 1; white-space: nowrap; }
  .person-title { font-size: 10px; color: var(--mint); letter-spacing: 1.5px; margin-top: 8px; margin-left: 70px; }

  .contact {
    position: absolute;
    display: flex; align-items: center; gap: 7px;
    font-size: 12.5px; color: var(--ink); white-space: nowrap;
  }
  .contact svg { width: 12px; height: 12px; flex: none; }
  .icon-square { width: 12px; height: 12px; border-radius: 2px; background: var(--mint); flex: none; }
  .phone { left: 30px; top: 30px; }
  .web { left: 30px; top: 226px; }
  .social { left: 30px; top: 256px; }
  .email { right: 30px; top: 226px; }
</style>
</head>
<body>
<main class="stage">
  <section class="card card-front" aria-label="Card front">
    <div class="front-mark">
      <span class="mark-dot"></span>
      <span class="brand-name">Meadow and Rowan<br>Massage Studio</span>
    </div>
  </section>

  <section class="card card-back" aria-label="Card back">
    <div class="contact phone">
      <svg viewBox="0 0 12 12"><rect width="12" height="12" rx="2" fill="#7fd3bb"/><path d="M3.5 3c.5-.4 1-.3 1.3.2l.5 1c.2.4 0 .7-.3.9.4.9 1 1.5 1.9 1.9.2-.3.5-.5.9-.3l1 .5c.5.3.6.8.2 1.3-.6.6-1.4.7-2.3.3C5 8 4 7 3.5 5.3 3.1 4.4 3 3.6 3.5 3z" fill="#fff"/></svg>
      555.014.2270
    </div>
    <div class="back-mark">
      <span class="mark-dot"></span>
      <span class="brand-name">Meadow and Rowan<br>Massage Studio</span>
    </div>
    <div class="person">
      <p class="person-name">Elena Marsh</p>
      <p class="person-title">LMT</p>
    </div>
    <div class="contact web">
      <svg viewBox="0 0 12 12"><circle cx="6" cy="6" r="6" fill="#7fd3bb"/><g fill="none" stroke="#fff" stroke-width=".8"><ellipse cx="6" cy="6" rx="2.3" ry="4.6"/><path d="M1.4 6h9.2M2.2 3.6h7.6M2.2 8.4h7.6"/></g></svg>
      www.meadowandrowan.com
    </div>
    <div class="contact social">
      <span class="icon-square"></span>
      @meadowandrowan
    </div>
    <div class="contact email">
      <svg viewBox="0 0 12 12"><rect width="12" height="12" rx="2" fill="#7fd3bb"/><rect x="2.5" y="3.5" width="7" height="5" fill="none" stroke="#fff" stroke-width=".8"/><path d="M2.5 3.5 6 6.3l3.5-2.8" fill="none" stroke="#fff" stroke-width=".8"/></svg>
      hello@meadowandrowan.com
    </div>
  </section>
</main>
</body>
</html>
```